Design LUMAGuidance.com

Looking to build a business professional coach website arround Brightorchard.com , it will some standard pages, about me, a page or 2 on bright orchard, maybe with a download and email grab, contact me....

```html
<!DOCTYPE html>
<html lang="en">
<head>
<meta charset="utf-8">
<title>Luma Guidance – Bright Orchard</title>
<link rel="stylesheet" href="https://fonts.googleapis.com/css2?family=Poppins:wght@400;500;600;700&display=swap">
<style>
:root{
  --purple:#4d2a86;
  --purple-deep:#3a1f6b;
  --purple-band:#5b3196;
  --green:#8dc21f;
  --orange:#f39c12;
  --blue:#1a7fd1;
  --brown:#8a5a2b;
  --ink:#222;
  --grey:#8a8a8a;
  --white:#fff;
  --black:#050505;
}
*{box-sizing:border-box;margin:0;padding:0}
html,body{width:1200px;height:3515px;overflow:hidden}
body{position:relative;font-family:"Poppins",sans-serif;color:var(--ink);background:var(--white)}
.abs{position:absolute}
.btn{position:absolute;background:var(--green);color:var(--white);border-radius:24px;display:flex;align-items:center;justify-content:center;font-size:16px;font-weight:400}

/* header */
.topline{left:0;top:0;width:1200px;height:5px;background:var(--purple)}
.brand{left:112px;top:28px;display:flex;align-items:center;gap:12px}
.brand-mark{width:26px;height:26px;background:var(--green)}
.brand-name{font-size:33px;font-weight:700;color:var(--purple);line-height:1}
.brand-tag{font-size:14px;color:var(--grey);line-height:1;margin-top:2px}
.nav a{position:absolute;top:38px;font-size:16px;color:var(--ink);text-decoration:none}
.search{left:868px;top:33px}

/* hero */
.hero{left:0;top:90px;width:1200px;height:601px;background:linear-gradient(90deg,#4a2480 0%,#55308a 35%,#3b2a45 60%,#5a4430 80%,#3a2c40 100%)}
.hero-overlay{left:0;top:90px;width:1200px;height:601px;background:linear-gradient(90deg,rgba(80,36,140,.85) 0%,rgba(80,36,140,.55) 45%,rgba(80,36,140,.15) 75%,rgba(80,36,140,.3) 100%)}
.hero-welcome{left:112px;top:188px;font-size:27px;font-weight:500;color:var(--white)}
.hero-title{left:110px;top:228px;font-size:62px;font-weight:700;line-height:82px;color:var(--white)}
.hero-text{left:112px;top:410px;width:680px;font-size:26px;line-height:43px;color:var(--white)}

/* how it works */
.section-title{font-size:40px;font-weight:700;color:var(--purple)}
.how-title{left:112px;top:782px}
.how-text{left:113px;top:852px;width:430px;font-size:15.5px;line-height:30px;color:var(--ink)}
.how-text p+p{margin-top:19px}
.frame-blue{left:928px;top:990px;width:172px;height:184px;background:var(--blue);border-radius:0 0 18px 18px}
.frame-orange{left:587px;top:973px;width:100px;height:210px;background:var(--orange);border-radius:18px 0 0 18px}
.photo{border-radius:18px}
.how-photo-a{left:650px;top:777px;width:441px;height:386px;background:linear-gradient(160deg,#5a4a42,#2c2a2e 50%,#6b5440)}
.how-photo-b{left:598px;top:984px;width:310px;height:272px;background:linear-gradient(170deg,#6b7680,#9aa3aa 40%,#2a2d33)}

/* services */
.services-title{left:0;width:1200px;top:1336px;text-align:center}
.card-photo{width:302px;height:214px;top:1424px;border-radius:12px 12px 0 0}
.card{top:1613px;width:283px;height:220px;background:var(--white);box-shadow:0 2px 8px rgba(0,0,0,.12);text-align:center}
.card h3{margin-top:24px;font-size:21px;font-weight:600}
.card p{margin:12px auto 0;width:230px;font-size:15.5px;line-height:26px;color:var(--ink)}
.card svg{margin-top:8px}
.card--orange{border-bottom:4px solid var(--orange)} .card--orange h3{color:var(--orange)}
.card--blue{border-bottom:4px solid var(--blue)} .card--blue h3{color:var(--blue)}
.card--brown{border-bottom:4px solid var(--brown)} .card--brown h3{color:var(--brown)}

/* benefits band */
.band{left:0;top:1922px;width:1200px;height:371px;background:linear-gradient(90deg,#5a3295,#6a3fa3 30%,#5b3399 60%,#6b40a6)}
.benefit{top:1980px;width:300px;text-align:center;color:var(--white)}
.benefit h3{font-size:23px;font-weight:600}
.benefit .icon{width:80px;height:80px;border-radius:50%;background:var(--white);margin:18px auto 0;display:flex;align-items:center;justify-content:center;box-shadow:0 0 0 4px rgba(255,255,255,.35)}
.benefit p{margin:26px auto 0;width:250px;font-size:16.5px;line-height:26px}

/* clients */
.clients-title{left:0;width:1200px;top:2370px;text-align:center}
.client-ring{left:458px;top:2459px;width:283px;height:283px;border-radius:50%;border:9px solid var(--green);background:var(--white);padding:6px}
.client-photo{width:100%;height:100%;border-radius:50%;background:linear-gradient(180deg,#8a9aa6,#3d4d63 60%,#1f2c44)}
.client-quote{left:312px;top:2768px;width:576px;text-align:center;font-size:16px;line-height:26px}

/* newsletter + footer */
.footer-bg{left:0;top:3070px;width:1200px;height:445px;background:var(--black)}
.newsletter{left:186px;top:2978px;width:830px;height:206px;background:var(--white);box-shadow:0 0 6px rgba(0,0,0,.1)}
.newsletter h2{margin-top:42px;text-align:center;font-size:40px;font-weight:700;color:var(--black)}
.subscribe{position:absolute;left:207px;top:116px;width:414px;height:45px;border:1.5px solid var(--green);border-radius:24px;display:flex;align-items:center}
.subscribe span{padding-left:22px;font-size:12px;color:var(--ink);flex:1}
.subscribe b{width:152px;height:45px;margin-right:-1.5px;background:var(--green);border-radius:24px;color:var(--white);font-weight:400;font-size:16px;display:flex;align-items:center;justify-content:center}
.footer-brand{left:0;width:1200px;top:3228px;text-align:center}
.footer-brand .mark{width:30px;height:30px;background:var(--green);margin:0 auto 10px}
.footer-brand .name{font-size:26px;font-weight:700;color:var(--purple);line-height:1}
.footer-brand .tag{font-size:11px;color:var(--purple);letter-spacing:2px;margin-top:4px}
.footer-nav a{position:absolute;top:3347px;font-size:16px;color:var(--white);text-decoration:none}
.social{top:3388px;width:22px;height:22px;background:var(--white);border-radius:3px}
.footer-rule{left:0;top:3458px;width:1200px;height:1px;background:#555}
.copyright{left:0;width:1200px;top:3478px;text-align:center;color:var(--white);font-size:14px}
</style>
</head>
<body>

<div class="abs topline"></div>
<header>
  <div class="abs brand">
    <div class="brand-mark"></div>
    <div>
      <div class="brand-name">LUMA GUIDANCE</div>
      <div class="brand-tag">Bright Orchard</div>
    </div>
  </div>
  <nav class="nav">
    <a style="left:496px">Home</a>
    <a style="left:567px">About Us</a>
    <a style="left:660px">Services</a>
    <a style="left:748px">Contact Us</a>
  </nav>
  <svg class="abs search" width="30" height="30" viewBox="0 0 30 30" aria-label="Search">
    <circle cx="12" cy="12" r="9" fill="none" stroke="var(--purple)" stroke-width="2.5"/>
    <line x1="18.5" y1="18.5" x2="27" y2="27" stroke="var(--purple)" stroke-width="3" stroke-linecap="round"/>
  </svg>
  <div class="btn" style="left:917px;top:26px;width:171px;height:42px">Contact Me</div>
</header>

<section>
  <div class="abs hero" role="img" aria-label="Speaker with headset addressing a large audience in a conference hall"></div>
  <div class="abs hero-overlay"></div>
  <div class="abs hero-welcome">Welcome to</div>
  <h1 class="abs hero-title">Luma Guidance<br>Bright Orchard</h1>
  <p class="abs hero-text">Lorem ipsum dolor sit amet, consectetur adipiscing elit, sed do eiusmod tempor incididunt ut labore et dolore magna aliqua.</p>
  <div class="btn" style="left:112px;top:573px;width:171px;height:43px">Download</div>
</section>

<section>
  <h2 class="abs section-title how-title">How it works</h2>
  <div class="abs how-text">
    <p>Ut enim ad minim veniam, quis nostrud exercitation ullamco laboris nisi ut aliquip ex ea commodo consequat. Duis aute irure dolor in reprehenderit in voluptate velit esse cillum dolore eu fugiat nulla pariatur.</p>
    <p>Sed ut perspiciatis unde omnis iste natus error sit voluptatem accusantium doloremque laudantium, totam rem aperiam, eaque ipsa quae ab illo inventore veritatis et quasi architecto beatae vitae dicta sunt explicabo.</p>
  </div>
  <div class="btn" style="left:113px;top:1197px;width:171px;height:43px">Read More</div>
  <div class="abs frame-blue"></div>
  <div class="abs frame-orange"></div>
  <div class="abs photo how-photo-a" role="img" aria-label="Audience seated in a seminar seen from behind"></div>
  <div class="abs photo how-photo-b" role="img" aria-label="Audience facing a projection screen during a presentation"></div>
</section>

<section>
  <h2 class="abs section-title services-title">Our Services</h2>
  <svg class="abs" style="left:54px;top:1505px" width="38" height="38" viewBox="0 0 38 38" aria-label="Previous"><circle cx="19" cy="19" r="17" fill="none" stroke="var(--brown)" stroke-width="2.5"/><path d="M22 11l-8 8 8 8" fill="none" stroke="var(--brown)" stroke-width="2.5"/></svg>
  <svg class="abs" style="left:1107px;top:1505px" width="38" height="38" viewBox="0 0 38 38" aria-label="Next"><circle cx="19" cy="19" r="17" fill="none" stroke="var(--brown)" stroke-width="2.5"/><path d="M16 11l8 8-8 8" fill="none" stroke="var(--brown)" stroke-width="2.5"/></svg>

  <div class="abs card-photo" style="left:112px;background:linear-gradient(150deg,#6b4a36,#2b2b30 50%,#9a7a5a)" role="img" aria-label="Speaker holding a microphone before an audience"></div>
  <div class="abs card-photo" style="left:450px;background:linear-gradient(170deg,#b5552a,#5a2a1e 45%,#7a2430)" role="img" aria-label="Presenter on stage facing a full auditorium"></div>
  <div class="abs card-photo" style="left:788px;background:linear-gradient(160deg,#6b5548,#3c4048 50%,#5a6470)" role="img" aria-label="Trainer presenting at a flip chart to a seated group"></div>

  <div class="abs card card--orange" style="left:124px">
    <h3>Coaching</h3>
    <p>Excepteur sint occaecat cupidatat non proident, sunt in culpa qui officia deserunt mollit anim id est laborum.</p>
    <svg width="36" height="16" viewBox="0 0 36 16"><path d="M1 8h33M26 1l8 7-8 7" fill="none" stroke="var(--orange)" stroke-width="2"/></svg>
  </div>
  <div class="abs card card--blue" style="left:462px">
    <h3>Learning</h3>
    <p>Duis aute irure dolor in reprehenderit in voluptate velit esse cillum dolore eu fugiat nulla pariatur.</p>
    <svg width="36" height="16" viewBox="0 0 36 16"><path d="M1 8h33M26 1l8 7-8 7" fill="none" stroke="var(--blue)" stroke-width="2"/></svg>
  </div>
  <div class="abs card card--brown" style="left:800px">
    <h3>Software</h3>
    <p>Excepteur sint occaecat cupidatat non proident, sunt in culpa qui officia deserunt mollit anim id est laborum.</p>
    <svg width="36" height="16" viewBox="0 0 36 16"><path d="M1 8h33M26 1l8 7-8 7" fill="none" stroke="var(--brown)" stroke-width="2"/></svg>
  </div>
</section>

<section>
  <div class="abs band" role="img" aria-label="Smiling woman in glasses behind a purple tint"></div>
  <div class="abs benefit" style="left:82px">
    <h3>More Money</h3>
    <div class="icon"><svg width="34" height="34" viewBox="0 0 34 34"><circle cx="17" cy="13" r="10" fill="none" stroke="var(--brown)" stroke-width="2.5"/><text x="17" y="18" text-anchor="middle" font-size="13" font-family="Poppins,sans-serif" font-weight="700" fill="var(--brown)">$</text><path d="M5 30h24" stroke="var(--brown)" stroke-width="3"/></svg></div>
    <p>Excepteur sint occaecat cupidatat non proident, sunt in culpa qui officia deserunt mollit anim id est laborum</p>
  </div>
  <div class="abs benefit" style="left:449px">
    <h3>More Time</h3>
    <div class="icon"><svg width="34" height="34" viewBox="0 0 34 34"><circle cx="17" cy="17" r="13" fill="none" stroke="var(--blue)" stroke-width="2.5" stroke-dasharray="60 8"/><path d="M17 9v8h6" fill="none" stroke="var(--blue)" stroke-width="2.5"/></svg></div>
    <p>Duis aute irure dolor in reprehenderit in voluptate velit esse cillum dolore eu fugiat nulla pariatur.</p>
  </div>
  <div class="abs benefit" style="left:816px">
    <h3>More Fun</h3>
    <div class="icon"><svg width="34" height="34" viewBox="0 0 34 34"><rect x="9" y="3" width="16" height="12" rx="2" fill="var(--orange)"/><circle cx="10" cy="21" r="4" fill="var(--orange)"/><circle cx="24" cy="21" r="4" fill="var(--orange)"/><path d="M3 33c0-5 3-7 7-7s7 2 7 7zM17 33c0-5 3-7 7-7s7 2 7 7z" fill="var(--orange)"/></svg></div>
    <p>Excepteur sint occaecat cupidatat non proident, sunt in culpa qui officia deserunt mollit anim id est laborum</p>
  </div>
</section>

<section>
  <h2 class="abs section-title clients-title">Our Clients</h2>
  <svg class="abs" style="left:54px;top:2582px" width="38" height="38" viewBox="0 0 38 38" aria-label="Previous"><circle cx="19" cy="19" r="17" fill="none" stroke="var(--brown)" stroke-width="2.5"/><path d="M22 11l-8 8 8 8" fill="none" stroke="var(--brown)" stroke-width="2.5"/></svg>
  <svg class="abs" style="left:1107px;top:2582px" width="38" height="38" viewBox="0 0 38 38" aria-label="Next"><circle cx="19" cy="19" r="17" fill="none" stroke="var(--brown)" stroke-width="2.5"/><path d="M16 11l8 8-8 8" fill="none" stroke="var(--brown)" stroke-width="2.5"/></svg>
  <div class="abs client-ring"><div class="client-photo" role="img" aria-label="Portrait of a client in a navy suit, arms folded, in an office"></div></div>
  <p class="abs client-quote">Sed ut perspiciatis unde omnis iste natus error sit voluptatem accusantium doloremque laudantium, totam rem aperiam, eaque ipsa quae ab illo inventore veritatis et quasi architecto beatae vitae dicta sunt explicabo. Excepteur sint occaecat cupidatat non proident, sunt in culpa qui officia deserunt mollit anim id est laborum.</p>
</section>

<footer>
  <div class="abs footer-bg"></div>
  <div class="abs newsletter">
    <h2>Subscribe Newsletter</h2>
    <div class="subscribe"><span>Enter &nbsp;Your Email</span><b>Subscribe</b></div>
  </div>
  <div class="abs footer-brand">
    <div class="mark"></div>
    <div class="name">LUMA GUIDANCE</div>
    <div class="tag">PROVEN STRATEGIES</div>
  </div>
  <nav class="footer-nav">
    <a style="left:343px">Home</a>
    <a style="left:435px">About Us</a>
    <a style="left:549px">Services</a>
    <a style="left:658px">Testimonial</a>
    <a style="left:792px">Contact</a>
  </nav>
  <div class="abs social" style="left:546px" aria-label="Social link"></div>
  <div class="abs social" style="left:589px" aria-label="Social link"></div>
  <div class="abs social" style="left:632px" aria-label="Social link"></div>
  <div class="abs footer-rule"></div>
  <div class="abs copyright">Copyright © 2023 Luma Guidance Bright Orchard. All Rights Reserved.</div>
</footer>

</body>
</html>
```